Pool Website

Need a simple front page and one internal page for a pool construction website. Please read the Must Have section for info. We uploaded 2 logos, one with color and one black and white. The colors you use in the logo can be changed, we used Century Gothic for the typing under the logo.

Nice clean design. The main back behind the site can be any color but we want the content back ground to be white.

We want a scrolling photo gallery (it doesn't have to scroll in your sample just know that's what we are envisioning) on the front page and the menu, and maybe a couple of photos down below to be clicked on such as this http://www.dellmorepools.example/

The 2ndary page would still have a header and menu and some type of cool design. Could be similar to this http://www.dellmorepools.example/about-us/awards.html

Also some other designs they like are here http://www.trelvacraft.example/14-examples-of-clean-modern-website-design-inspiration/ I realize not all of these could have a image scroller on the front page which is fine.

Please do not copy their site exactly though it must be different.

For now you can just use sample stock photography for your photos for the design but ultimately we will swap them out for our own photos so there will not be a need to purchase stock photography of pools.

Menus will include Home - About - Services - Gallery - Contact - Blog

The current site is http://www.gilesfentonpools.example/ we do not want it to look anything like this. It's way too dark and just not professional looking. We want this new site to look very slick and professional.

We also want a space for social networking logos etc.

I have also attached 2 zip files that contain photos that may be used in the design. You do not have to use them all but you are welcome to use a few. Most will be put in the photo gallery.

Colors: Blues, white, grays, black, etc.
Updates

Added several photos that can be used in the design. Obviously you do not have to use them all most will be in the photo gallery but you're welcome to use some for your design. 

Target Market(s)

People with money for residential pools or companies that want corporate pools. Are target location is Miami and California

Industry/Entity Type

Construction

Font styles to use
Serif
Sans Serif

Requirements
Must have
• Nice clean design. The main back behind the site can be any color but we want the content back ground to be white.

```html
<!DOCTYPE html>
<html lang="en">
<head>
<meta charset="utf-8">
<title>Giles Fenton Pools</title>
<link href="https://fonts.googleapis.com/css2?family=Arimo:wght@400;700&family=Questrial&family=Kaushan+Script&display=swap" rel="stylesheet">
<style>
:root{
  --navy:#141f78;
  --navy-deep:#0e1760;
  --gray-band:#dcdcdc;
  --white:#ffffff;
  --text-navy:#1a237e;
  --rule:#3a48a0;
}
*{box-sizing:border-box;margin:0;padding:0}
html,body{width:960px;height:1200px;overflow:hidden}
body{position:relative;background:var(--white);font-family:Arimo,Arial,sans-serif;color:var(--text-navy)}
a{color:inherit;text-decoration:none}

.topbar{position:absolute;left:0;top:0;width:960px;height:66px;
  background:linear-gradient(180deg,#5aa0ff 0%,#2d6be0 35%,#1b3fb5 70%,var(--navy) 100%)}
.tagline{position:absolute;left:143px;top:19px;width:240px;white-space:nowrap;font-family:"Kaushan Script",cursive;font-size:17px;line-height:22px;color:var(--white)}
.menu{position:absolute;top:0;left:0;width:960px;height:100%;font-family:Questrial,sans-serif;font-size:14px;line-height:18px;color:var(--white)}
.menu a{position:absolute;white-space:nowrap}
.topbar .menu a{top:25px}
.m-home{left:422px}.m-about{left:478px}.m-services{left:534px}.m-gallery{left:598px}.m-contact{left:662px}.m-blog{left:734px}
.social{position:absolute;display:flex;gap:11px}
.social span{display:block;width:20px;height:20px;border-radius:4px;background:var(--white)}
.topbar .social{left:791px;top:23px}

.brandband{position:absolute;left:0;top:66px;width:960px;height:146px;
  background:linear-gradient(90deg,#e4e4e4 0%,#ffffff 45%,#ffffff 55%,#e4e4e4 100%);
  border-top:2px solid #d0d0d0}
.brand{position:absolute;left:0;width:960px;top:44px;display:flex;flex-direction:column;align-items:center;gap:8px}
.brand-mark{width:34px;height:34px;background:var(--navy);border-radius:6px}
.brand-name{font-family:Questrial,sans-serif;font-size:15px;letter-spacing:1px;color:var(--navy)}

.hero{position:absolute;left:0;top:212px;width:960px;height:328px;background:var(--navy)}
.slider{position:absolute;left:120px;top:0;width:720px;height:238px;border:3px solid #d8dde8;border-top:none;border-radius:0 0 16px 16px;overflow:hidden;
  background:linear-gradient(180deg,#1d3f8c 0%,#6d5a4a 35%,#d9a46a 55%,#8a6a4c 72%,#29b5c8 88%,#1e8eb0 100%)}
.dots{position:absolute;left:325px;top:18px;width:64px;height:15px;border-radius:8px;background:rgba(20,20,40,.6);display:flex;justify-content:center;align-items:center;gap:4px}
.dots i{width:6px;height:6px;border-radius:50%;border:1px solid #fff}
.dots i.on{background:#fff}
.arrow{position:absolute;top:88px}
.arrow.prev{left:14px}.arrow.next{right:14px}
.welcome{position:absolute;left:120px;top:260px;width:474px;text-align:center;color:var(--white);font-size:19px;line-height:24px}
.welcome .strong{font-size:21px;font-weight:700}
.divider{position:absolute;left:600px;top:250px;width:1px;height:64px;background:var(--rule)}
.serving{position:absolute;left:647px;top:253px;color:var(--white);font-size:14.5px;line-height:17px}
.phone{position:absolute;left:632px;top:286px;display:flex;align-items:center;gap:6px;color:var(--white);font-weight:700;font-size:24px}

.cards{position:absolute;left:120px;top:585px;display:flex;gap:13px}
.card{width:231px;height:210px}
.card-head{height:79px;background:linear-gradient(180deg,#ffffff 0%,#e6edf8 100%);border-bottom:2px solid var(--navy);
  display:flex;align-items:center;justify-content:center;text-align:center;font-size:14px;line-height:16px;color:var(--navy)}
.card-photo{height:131px;border:2px solid var(--navy);border-top:none;border-radius:0 0 16px 16px}
.photo-1{background:linear-gradient(180deg,#4a5a3a 0%,#8a8f7a 40%,#2f6fb8 75%,#5aa7e0 100%)}
.photo-2{background:linear-gradient(180deg,#2a2418 0%,#7a5a38 45%,#1f4c6a 75%,#2a90b8 100%)}
.photo-3{background:linear-gradient(180deg,#8a8470 0%,#c9c3ae 40%,#3d7c9a 70%,#9aa6a0 100%)}

.intro{position:absolute;left:120px;top:814px;width:720px;text-align:center;font-size:11.5px;line-height:16px;color:var(--text-navy)}

.showroom{position:absolute;left:0;top:897px;width:362px;height:159px;background:var(--gray-band)}
.address{position:absolute;left:138px;top:47px;font-size:16px;line-height:19.5px;color:var(--navy)}
.address b{font-size:16.5px}
.map{position:absolute;left:362px;top:897px;width:598px;height:159px;background:linear-gradient(135deg,#ece9e2 0%,#e4e1d9 60%,#dcd8cf 100%)}

.footer{position:absolute;left:0;top:1056px;width:960px;height:144px;background:var(--navy);color:var(--white)}
.services{position:absolute;left:0;top:27px;width:960px;text-align:center;font-size:11.5px}
.services span{margin:0 7px}
.rule{position:absolute;left:122px;top:62px;width:718px;height:1px;background:var(--rule)}
.footer .menu a{top:97px}
.f-home{left:179px}.f-about{left:235px}.f-services{left:291px}.f-gallery{left:355px}.f-contact{left:419px}.f-blog{left:491px}
.footer .social{left:538px;top:90px;gap:10px}
.footer .social span{width:25px;height:25px}
.payments{position:absolute;left:672px;top:72px;width:168px;height:72px;background:var(--navy-deep);border-radius:6px 6px 0 0;text-align:center;font-size:11.5px;line-height:16px;padding-top:12px}
.payments .cards-accepted{display:flex;justify-content:center;gap:8px;margin-top:4px}
.payments .cards-accepted i{width:26px;height:12px;border-radius:2px;background:#c9cde6}
</style>
</head>
<body>

<header class="topbar">
  <div class="tagline">Family Owned for Over 30 Years!</div>
  <nav class="menu"><a class="m-home">Home</a><a class="m-about">About</a><a class="m-services">Services</a><a class="m-gallery">Gallery</a><a class="m-contact">Contact</a><a class="m-blog">Blog</a></nav>
  <div class="social"><span></span><span></span></div>
</header>

<section class="brandband">
  <div class="brand"><div class="brand-mark"></div><div class="brand-name">GILES FENTON POOLS</div></div>
</section>

<section class="hero">
  <div class="slider" role="img" aria-label="Luxury two-storey home at dusk with lit terrace and pool in front">
    <div class="dots"><i class="on"></i><i></i><i></i><i></i><i></i></div>
    <svg class="arrow prev" width="16" height="70" viewBox="0 0 16 70"><polyline points="15,2 2,35 15,68" fill="none" stroke="#fff" stroke-width="1.5"/></svg>
    <svg class="arrow next" width="16" height="70" viewBox="0 0 16 70"><polyline points="1,2 14,35 1,68" fill="none" stroke="#fff" stroke-width="1.5"/></svg>
  </div>
  <div class="welcome"><b>Welcome</b> to Giles Fenton Pool Contracting, Inc.<br><span class="strong">Your Ultimate Dealer!</span></div>
  <div class="divider"></div>
  <div class="serving">Serving Broward, Palm,<br>&amp; Miami-Dade Counties</div>
  <div class="phone">
    <svg width="14" height="18" viewBox="0 0 14 18"><path d="M3 1 L6 5 L4.5 7 Q6 11 9 13 L11 11.5 L13.5 14.5 L11.5 17 Q3 14 1 3 Z" fill="#3a4aa8"/></svg>
    954-555-0142
  </div>
</section>

<section class="cards">
  <div class="card"><div class="card-head"><span>Full Service<br><b>Pool Company</b></span></div><div class="card-photo photo-1" role="img" aria-label="Backyard pool with stone spillway and tropical garden"></div></div>
  <div class="card"><div class="card-head"><span><b>Residential</b> and<br><b>Commercial Pools</b><br>in South Florida</span></div><div class="card-photo photo-2" role="img" aria-label="Lit covered patio beside a free-form pool at night"></div></div>
  <div class="card"><div class="card-head"><span>Maintenance,<br><b>Repairs and Renovations</b></span></div><div class="card-photo photo-3" role="img" aria-label="Free-form pool with stone deck and fire bowl"></div></div>
</section>

<p class="intro">That's just some of the services we offer at <b>Giles Fenton Pool Contracting, Inc.</b> you'll find quality, selection, and <b>innovative planning</b> and construction no matter what your pool needs may be. Some of our clients are developers including <b>Calloway Homes, B.R.T. Communities, Marston Development, Northgate Homes and Whitcombe Homes</b>.</p>

<section class="showroom">
  <div class="address"><b>Visit our showroom</b><br>2470 NW 41 Court,<br>Harbor Pointe,<br>Florida 33099</div>
</section>
<div class="map" role="img" aria-label="Street map showing the showroom location"></div>

<footer class="footer">
  <div class="services">Commercial Pool Installation<span>I</span>Pool Maintenance<span>I</span>Pool Remodeling<span>I</span>Pool Renovation<span>I</span>Swimming Pool Installation<span>I</span>Pool Repair</div>
  <div class="rule"></div>
  <nav class="menu"><a class="f-home">Home</a><a class="f-about">About</a><a class="f-services">Services</a><a class="f-gallery">Gallery</a><a class="f-contact">Contact</a><a class="f-blog">Blog</a></nav>
  <div class="social"><span></span><span></span></div>
  <div class="payments">Payments Accepted<br>Cash, Personal Check
    <div class="cards-accepted"><i></i><i></i><i></i></div>
  </div>
</footer>

</body>
</html>
```